Playful Website Design Needed Pet Sitting and Dog Walking Business

Need a simple one page Web Design Built on WordPress.
Sections:

About Us
Services Provided
Costs
Contact Us
Intake Form (Questionnaire that goes to email)
See us in Action

Industry/Entity Type

Pet Sitting and Dog Walking

Number of Pages Required

1 page

Font styles to use
Other font styles liked:
• See the Business Card Font and use that.

Colors
EE7325
F08F49
F5BC92
FAE3D3
FDF4ED

Requirements
Must have
• See attached Logo Design, with Font's and Colors Use these as theme guide

```html
<!DOCTYPE html>
<html lang="en">
<head>
<meta charset="utf-8">
<title>Paws &amp; Petals Care</title>
<link rel="stylesheet" href="https://fonts.googleapis.com/css2?family=Short+Stack&display=swap">
<style>
:root{
  --orange:#EE7325;
  --orange-2:#F08F49;
  --peach:#F5BC92;
  --cream:#FAE3D3;
  --ivory:#FDF4ED;
  --yellow:#FFE100;
  --green:#7DBE3A;
  --ink:#2b2b2b;
  --dark:#55575a;
  --white:#ffffff;
}
*{box-sizing:border-box;margin:0;padding:0}
html,body{width:1200px;height:3868px;overflow:hidden}
body{position:relative;background:var(--white);font-family:"Short Stack",cursive;color:var(--ink)}
.abs{position:absolute}
.brand{font-size:30px;color:var(--green);line-height:1.1;display:flex;align-items:center;gap:12px;white-space:nowrap}
.brand .dot{width:26px;height:26px;border-radius:50%;background:var(--orange);flex:none}
.top-email{left:725px;top:58px;color:var(--orange);font-size:22px;display:flex;gap:10px;align-items:center}
.nav{left:418px;top:118px;display:flex;gap:30px;font-size:17px;white-space:nowrap}
.hero{left:0;top:185px;width:1200px;height:650px}
.hero-title{left:137px;top:350px;color:var(--white);font-size:58px;line-height:1.1}
.hero-list{left:137px;top:500px;list-style:none;color:var(--white);font-size:23px}
.hero-list li{display:flex;align-items:center;gap:14px;height:50px}
.hero-list li::before{content:"";width:12px;height:12px;background:var(--orange)}
.section-title{font-size:40px;line-height:1.15}
.body-text{font-size:13px;line-height:26px}
.about-title{left:622px;top:1010px;color:var(--orange)}
.about-title span{color:var(--green)}
.about-text{left:622px;top:1125px;width:400px}
.services-title{left:0;width:1200px;top:1590px;text-align:center;color:var(--white)}
.services-text{left:270px;width:660px;top:1660px;text-align:center;color:var(--white);font-size:13px;line-height:26px}
.svc-photo{width:210px;height:210px;border-radius:50%;border:5px solid var(--white)}
.svc-title{color:var(--white);font-size:27px}
.svc-text{color:var(--white);font-size:12px;line-height:26px;width:230px}
.costs-title{left:150px;top:2225px;color:var(--orange)}
.costs-text{left:150px;top:2282px;width:420px}
.costs-list{left:145px;top:2395px;list-style:none;color:var(--orange);font-size:23px}
.costs-list li{display:flex;align-items:center;gap:12px;height:50px}
.costs-list li::before{content:"";width:12px;height:12px;border-radius:50%;background:var(--green)}
.pill{left:275px;top:2645px;width:650px;height:86px;border-radius:43px;background:var(--orange);color:var(--white);font-size:19px;display:flex;align-items:center;justify-content:center;white-space:nowrap;padding:0 30px}
.contact-title{left:180px;top:2980px;color:var(--white)}
.contact-text{left:180px;top:3045px;width:420px;color:var(--white)}
.contact-list{left:180px;top:3150px;list-style:none;color:var(--white);font-size:15px;line-height:20px}
.contact-list li{display:flex;align-items:center;gap:16px;height:44px}
.contact-list .ico{width:38px;height:38px;border-radius:50%;background:var(--orange);display:flex;align-items:center;justify-content:center;flex:none}
.form{left:652px;top:2955px;width:418px;height:460px;background:var(--white);border-radius:120px 80px 0 120px;padding:0 52px}
.form label{display:block;font-size:15px;color:#555;margin:28px 0 8px}
.form .field{height:40px;border-radius:8px;background:#f3f3f3;border:1px solid #e6e6e6}
.form .field.msg{height:118px}
.form .submit{margin:26px auto 0;width:172px;height:48px;border-radius:16px;background:var(--orange);color:var(--white);font-size:20px;display:flex;align-items:center;justify-content:center}
.footer-brand{left:0;width:1200px;top:3680px;justify-content:center}
.footer-email{left:0;width:1200px;top:3752px;justify-content:center;color:var(--orange);font-size:22px;display:flex;gap:10px;align-items:center}
.copyright{left:0;width:1200px;top:3797px;text-align:center;font-size:16px}
</style>
</head>
<body>

<!-- header -->
<svg class="abs" style="left:940px;top:0" width="260" height="150" viewBox="0 0 260 150" aria-hidden="true"><path d="M0 0 H260 V150 C230 80 150 70 90 60 C40 50 10 30 0 0Z" fill="var(--orange)"/></svg>
<div class="abs brand" style="left:145px;top:80px"><span class="dot"></span>Paws &amp; Petals Care</div>
<div class="abs top-email">
  <svg width="30" height="22" viewBox="0 0 30 22" aria-hidden="true"><rect x="1.5" y="1.5" width="27" height="19" fill="none" stroke="var(--orange)" stroke-width="3"/><path d="M2 3 L15 13 L28 3" fill="none" stroke="var(--orange)" stroke-width="3"/></svg>
  hello@pawspetals.com
</div>
<nav class="abs nav"><span>About Us</span><span>Services Provided</span><span>Costs</span><span>Contact Us</span><span>See us in Action</span></nav>

<!-- hero -->
<svg class="abs hero" viewBox="0 0 1200 650" role="img" aria-label="Photo of a woman walking a golden dog on an autumn leaf path">
  <defs><linearGradient id="heroG" x1="0" y1="0" x2="1" y2="1"><stop offset="0" stop-color="#8a7a4a"/><stop offset=".5" stop-color="#c89a55"/><stop offset="1" stop-color="#d8782a"/></linearGradient></defs>
  <path d="M0 0H1200V560C900 620 700 640 600 640C400 640 200 600 0 565Z" fill="url(#heroG)"/>
  <path d="M100 595C350 640 500 650 600 650C760 650 950 620 1110 580C950 630 760 660 600 660C480 660 300 640 100 595Z" fill="var(--orange)"/>
</svg>
<div class="abs" style="left:590px;top:785px;width:80px;height:80px;border-radius:50%;background:var(--orange)"></div>
<h1 class="abs section-title hero-title">Paws &amp; Petals<br>Care</h1>
<ul class="abs hero-list"><li>8$ per visit. 2 visits a day.</li><li>All pets, Any Age!</li><li>Parent surpervised.</li></ul>

<!-- about -->
<svg class="abs" style="left:195px;top:975px" width="390" height="390" viewBox="0 0 390 390" role="img" aria-label="Photo of a woman hugging a small dog inside a blob frame">
  <path d="M60 40C150 -10 300 10 360 110C400 200 330 380 230 385C120 390 20 330 15 220C10 140 20 60 60 40Z" fill="var(--yellow)"/>
  <path d="M70 30C160 -5 310 30 350 130C380 220 300 370 200 370C100 370 10 300 20 200C25 120 30 50 70 30Z" fill="var(--orange)"/>
  <path d="M90 40C170 0 300 40 330 140C350 230 280 340 190 340C110 340 10 280 10 190C10 120 50 60 90 40Z" fill="#8a6a55"/>
</svg>
<h2 class="abs section-title about-title">About Paws &amp;<br><span>Petals Care</span></h2>
<p class="abs body-text about-text">Lorem ipsum dolor sit amet, consectetur adipiscing elit, sed do eiusmod tempor incididunt ut labore et dolore magna aliqua. Quis ipsum suspendisse ultrices gravida. Risus commodo viverra maecenas.</p>
<div class="abs" style="left:985px;top:1290px;width:170px;height:175px;border-radius:50%;background:var(--orange-2)" role="img" aria-label="Smiling flower character illustration"></div>

<!-- services -->
<svg class="abs" style="left:0;top:1440px" width="1200" height="690" viewBox="0 0 1200 690" role="img" aria-label="Orange to yellow painted band with faint floral pattern">
  <defs><linearGradient id="svcG" x1="0" x2="1"><stop offset="0" stop-color="var(--orange)"/><stop offset=".45" stop-color="#f7a21a"/><stop offset="1" stop-color="var(--yellow)"/></linearGradient></defs>
  <path d="M0 20L40 30L90 10L150 28L220 12L300 30L380 14L460 26L540 8L620 28L700 12L780 26L860 10L940 30L1020 12L1100 28L1200 14V660L1140 675L1060 655L980 680L900 660L820 678L740 658L660 682L580 660L500 676L420 656L340 680L260 660L180 676L100 656L40 672L0 660Z" fill="url(#svcG)"/>
</svg>
<h2 class="abs section-title services-title">Services Provided</h2>
<p class="abs services-text">Lorem ipsum dolor sit amet, consectetur adipiscing elit, sed do eiusmod tempor incididunt ut labore et dolore magna aliqua. Quis ipsum suspendisse ultr</p>
<div class="abs svc-photo" style="left:150px;top:1768px;background:#b58560" role="img" aria-label="Photo of a woman playing with a ginger cat"></div>
<h3 class="abs svc-title" style="left:378px;top:1790px">Pet Sitting</h3>
<p class="abs svc-text" style="left:378px;top:1840px">Lorem ipsum dolor sit amet, consectetur adipiscing elit, sed do eiusmod tempor incididunt ut labore et</p>
<div class="abs svc-photo" style="left:612px;top:1768px;background:#d9d2c8" role="img" aria-label="Photo of a woman walking a dog on the beach"></div>
<h3 class="abs svc-title" style="left:838px;top:1790px">Dog Walking</h3>
<p class="abs svc-text" style="left:838px;top:1840px">Lorem ipsum dolor sit amet, consectetur adipiscing elit, sed do eiusmod tempor incididunt ut labore et</p>

<!-- costs -->
<h2 class="abs section-title costs-title">Costs</h2>
<p class="abs body-text costs-text">Lorem ipsum dolor sit amet, consectetur adipiscing elit, sed do eiusmod tempor incididunt ut labore et dolore magna aliqua.</p>
<ul class="abs costs-list"><li>8$ per visit. 2 visits a day.</li><li>All pets, Any Age!</li><li>Parent surpervised.</li></ul>
<div class="abs" style="left:638px;top:2213px;width:380px;height:382px;border-radius:190px 190px 0 190px;background:linear-gradient(160deg,#9cc45a,#5f8f2e)" role="img" aria-label="Photo of a kitten and a dog playing on grass"></div>
<div class="abs" style="left:68px;top:2540px;width:180px;height:255px;border-radius:50%;background:var(--orange-2)" role="img" aria-label="Smiling flower character illustration"></div>
<div class="abs pill">we feed, walk and play with your pet, each visit!</div>

<!-- contact -->
<svg class="abs" style="left:0;top:2825px" width="1200" height="700" viewBox="0 0 1200 700" role="img" aria-label="Dark band with a faded photo of a dog">
  <path d="M0 110C300 20 800 -10 1200 60V640C800 700 300 690 0 600Z" fill="var(--dark)"/>
  <path d="M0 95C320 10 780 -15 1200 40V58C780 5 320 25 0 115Z" fill="var(--green)"/>
  <path d="M500 8C780 -5 1000 20 1200 60V80C1000 40 780 15 500 20Z" fill="var(--orange)"/>
  <path d="M0 600C300 690 800 700 1200 640V660C800 720 300 710 0 620Z" fill="var(--green)"/>
  <path d="M0 612C300 702 700 712 1000 685C700 725 300 715 0 625Z" fill="var(--orange)"/>
</svg>
<h2 class="abs section-title contact-title">Contact Us</h2>
<p class="abs body-text contact-text">Lorem ipsum dolor sit amet, consectetur adipiscing elit, sed do eiusmod tempor incididunt ut labore et dolore magna aliqua.</p>
<ul class="abs contact-list">
  <li><span class="ico"><svg width="16" height="20" viewBox="0 0 16 20"><path d="M8 0C3.6 0 0 3.4 0 7.6 0 13 8 20 8 20S16 13 16 7.6C16 3.4 12.4 0 8 0Z" fill="#fff"/><circle cx="8" cy="7.5" r="3" fill="var(--orange)"/></svg></span>418 Maple Grove Lane,<br>Riverton, WI 53100</li>
  <li><span class="ico"><svg width="18" height="18" viewBox="0 0 24 24"><path d="M6.6 10.8a15 15 0 006.6 6.6l2.2-2.2c.3-.3.7-.4 1-.2 1.1.4 2.3.6 3.6.6.6 0 1 .4 1 1V20c0 .6-.4 1-1 1C10.6 21 3 13.4 3 4c0-.6.4-1 1-1h3.5c.6 0 1 .4 1 1 0 1.3.2 2.5.6 3.6.1.3 0 .7-.2 1z" fill="#fff"/></svg></span>Phone: 555-201-4470</li>
  <li><span class="ico"><svg width="18" height="18" viewBox="0 0 18 18"><rect x="4" y="1" width="10" height="5" fill="#fff"/><rect x="1" y="6" width="16" height="11" rx="2" fill="#fff"/><rect x="5" y="10" width="8" height="2" fill="var(--orange)"/></svg></span>Fax : 555-201-4471</li>
  <li><span class="ico"><svg width="18" height="14" viewBox="0 0 18 14"><rect width="18" height="14" rx="2" fill="#fff"/><path d="M1 1L9 8L17 1" fill="none" stroke="var(--orange)" stroke-width="2"/></svg></span>Email Address:<br>info@pawspetals.com</li>
</ul>
<div class="abs form">
  <label>Name:</label><div class="field"></div>
  <label>Email:</label><div class="field"></div>
  <label>Message:</label><div class="field msg"></div>
  <div class="submit">Submit Now</div>
</div>

<!-- footer -->
<svg class="abs" style="left:0;top:3740px" width="260" height="128" viewBox="0 0 260 128" aria-hidden="true"><path d="M0 0C20 60 100 100 260 128H0Z" fill="var(--orange)"/></svg>
<div class="abs brand footer-brand"><span class="dot"></span>Paws &amp; Petals Care</div>
<div class="abs footer-email">
  <svg width="30" height="22" viewBox="0 0 30 22" aria-hidden="true"><rect x="1.5" y="1.5" width="27" height="19" fill="none" stroke="var(--orange)" stroke-width="3"/><path d="M2 3 L15 13 L28 3" fill="none" stroke="var(--orange)" stroke-width="3"/></svg>
  hello@pawspetals.com
</div>
<p class="abs copyright">2022 All Rights Reserved .</p>
<div class="abs" style="left:950px;top:3600px;width:175px;height:268px;border-radius:50% 50% 0 0;background:var(--orange-2)" role="img" aria-label="Smiling flower character illustration"></div>

</body>
</html>
```